Brindle Logistics Business Card Design

We are a trucking and warehousing company. We run freight in the US manly from the Pacific NW to TX and back up the the PNW. We also do warehousing where we store, move, and distribute freight. Looking for a clean and modern design of business card. We would like to look rich and elegant. Attached is our logo.

Industry/Entity Type

Trucking Company

Contact Information for Business Card

Looking for a clean and modern design of business card. We would like to look rich and elegant.

Font styles to use
Sans Serif

Colors

Designer to choose colors to be used in the design.

Requirements
Must have
• logo but it should not dominate the card
Should not have
• logo should not dominate the card

```html
<!DOCTYPE html>
<html lang="en">
<head>
<meta charset="utf-8">
<title>Brindle Logistics – Business Card</title>
<link href="https://fonts.googleapis.com/css2?family=Arimo:wght@400;700&display=swap" rel="stylesheet">
<style>
  :root {
    --orange: #e38a1f;
    --orange-deep: #c9771a;
    --charcoal: #363638;
    --paper: #f2f2f2;
    --paper-shade: #d9d9d9;
    --ink: #2c3440;
    --blue: #1b6fb8;
    --stage: #c4c4c4;
    --white: #ffffff;
  }
  * { margin: 0; padding: 0; box-sizing: border-box; }
  html, body {
    width: 1200px; height: 862px; overflow: hidden;
    background: var(--stage);
    font-family: "Arimo", Arial, sans-serif;
  }
  .card {
    position: absolute;
    width: 560px; height: 320px;
    overflow: hidden;
    box-shadow: 0 6px 18px rgba(0,0,0,.25);
  }
  .card svg.art { position: absolute; inset: 0; }
  .card-back { left: 70px; top: 80px; }
  .card-front { left: 570px; top: 462px; }

  .web {
    position: absolute;
    color: var(--white);
    white-space: nowrap;
  }
  .card-back .web { left: 175px; top: 256px; font-size: 18px; letter-spacing: 4px; }
  .card-front .web { left: 175px; top: 259px; font-size: 16px; letter-spacing: 3px; }

  .brand-block { position: absolute; left: 22px; top: 64px; color: var(--ink); }
  .brand-name { font-size: 22px; font-weight: 700; }
  .brand-tag { font-size: 11px; margin-top: 1px; }

  .contacts { position: absolute; left: 112px; top: 132px; list-style: none; }
  .contacts li {
    display: flex; align-items: center; gap: 12px;
    font-size: 14px; color: var(--ink); height: 36px;
  }
  .contacts svg { width: 24px; height: 24px; }

  .logo-plate {
    position: absolute; right: 22px; top: 22px;
    background: var(--white); padding: 6px 10px;
    display: flex; align-items: center; gap: 8px;
  }
  .logo-plate .dot { width: 10px; height: 10px; background: var(--blue); }
  .logo-plate .name { color: var(--blue); font-size: 14px; font-weight: 700; letter-spacing: 1px; }
</style>
</head>
<body>

<section class="card card-back">
  <svg class="art" width="560" height="320" viewBox="0 0 560 320">
    <defs>
      <linearGradient id="roadGrad" x1="0" y1="0" x2="1" y2="0">
        <stop offset="0" stop-color="var(--orange)"/>
        <stop offset=".5" stop-color="var(--orange-deep)"/>
        <stop offset=".56" stop-color="var(--charcoal)"/>
        <stop offset="1" stop-color="var(--charcoal)"/>
      </linearGradient>
    </defs>
    <rect width="560" height="320" fill="var(--orange)"/>
    <rect class="road-illustration" x="0" y="0" width="560" height="222" fill="url(#roadGrad)" role="img" aria-label="Illustration of road lane markings splitting into route arrows"/>
    <rect x="0" y="222" width="560" height="26" fill="var(--orange)"/>
    <rect x="0" y="248" width="560" height="38" fill="var(--charcoal)"/>
    <rect x="330" y="286" width="230" height="34" fill="var(--charcoal)"/>
  </svg>
  <div class="web">www.website.com</div>
</section>

<section class="card card-front">
  <svg class="art" width="560" height="320" viewBox="0 0 560 320">
    <defs>
      <linearGradient id="paperGrad" x1="0" y1="0" x2="0" y2="1">
        <stop offset="0" stop-color="var(--paper-shade)"/>
        <stop offset="1" stop-color="var(--paper)"/>
      </linearGradient>
      <linearGradient id="photoGrad" x1="0" y1="0" x2="1" y2="1">
        <stop offset="0" stop-color="#7a6a5a"/>
        <stop offset=".45" stop-color="#e0a050"/>
        <stop offset="1" stop-color="#f6b560"/>
      </linearGradient>
    </defs>
    <rect width="560" height="320" fill="url(#paperGrad)"/>
    <polygon points="395,0 560,0 560,320 440,320" fill="var(--orange-deep)"/>
    <polygon points="410,70 560,70 560,320 440,320" fill="url(#photoGrad)" role="img" aria-label="Photo of a freight truck on an open highway"/>
    <polygon points="385,110 425,110 455,320 420,320 385,250" fill="#1d2430" opacity=".55"/>
    <polygon points="0,58 330,58 325,100 0,108" fill="var(--orange)"/>
    <rect x="0" y="246" width="440" height="4" fill="var(--orange)"/>
    <polygon points="0,250 440,250 432,290 0,290" fill="var(--charcoal)"/>
  </svg>

  <div class="logo-plate">
    <span class="dot"></span>
    <span class="name">BRINDLE LOGISTICS</span>
  </div>

  <div class="brand-block">
    <div class="brand-name">Brindle Logistics,LLC</div>
    <div class="brand-tag">Trucking and Warehousing</div>
  </div>

  <ul class="contacts">
    <li>
      <svg viewBox="0 0 24 24" fill="none" stroke="var(--blue)" stroke-width="2"><path d="M3 11 12 3l9 8M5 9v12h5v-6h4v6h5V9"/></svg>
      Company Address
    </li>
    <li>
      <svg viewBox="0 0 24 24" fill="none" stroke="var(--blue)" stroke-width="2"><path d="M5 4h4l2 5-3 2a11 11 0 0 0 5 5l2-3 5 2v4a2 2 0 0 1-2 2A17 17 0 0 1 3 6a2 2 0 0 1 2-2z"/></svg>
      Company phone
    </li>
    <li>
      <svg viewBox="0 0 24 24" fill="none" stroke="var(--blue)" stroke-width="2"><rect x="2" y="5" width="20" height="14"/><path d="m2 5 10 8 10-8M2 19l7-7M22 19l-7-7"/></svg>
      Company email
    </li>
  </ul>

  <div class="web">www.website.com</div>
</section>

</body>
</html>
```